Now hiring billboard for roofing company

We would like to design/slogan for a "now hiring" billboard for a variety of positions in our roofing company.
We perform residential and commercial roofing.
We are looking to hire roofers, laborers, gutter installers, sheet metal workers, commercial drivers, commercial roofers, and residential and commercial service technicians.
Looking to attract both entry level and experienced roofers.
Roofing is a good industry to build a career, learn a trade, we provide training.

Opportunity to learn a trade and move from unskilled to skilled positions.
Use Brantley Roofing as a stepping stone in your career.

Brantley Roofing is a stable, growing company that has been providing roofing services in the Portland area for over 35 years. We have a great team of employees, many with over 10 years with the company.
In addition to roofing homes, our Residential Department also offers repair and cleaning services as well as gutter installation and repair.
In 2014 we added a dedicated Commercial Department that services commercial customers with roofing projects and service/repairs. In addition, they offer the Brantley topGuard maintenance program.
Mostly recently Brantley Roofing purchased Voskuil Sheet Metal (VSM) in 2016. VSM specializes in custom metal fabrication, continuous gutters and custom copper fabrication.

If you are looking for a job where you are appreciated
at a company that values honesty and respect,
come and join our team!
Whether you are experienced or just wanting to
learn, we are looking to add hard-working, reliable
go-getters to our team. We offer a flexible work
environment and in addition to full-time work offer
part-time and summer positions.
We are always looking to add great people to our
team. Some of the job/career options are:
• Residential Roofer
• Commercial Roofer
• Gutter Installer
• Service Technician
• Sheet Metal Fabricator/Installer
• Commercial Driver
• General Labor

Brantley Roofing offers competitive pay and an excellent benefits package.

Join our team today!

Target Market(s)

Job seekers

Font styles to use
Serif

Colors

Designer to choose colors to be used in the design.

Requirements
Must have
• Get across that we are hiring and have our contact info
• CCB #62813
• brantleywork.example
Nice to have
• Simple, easy to understand regardless of language literacy.
• Have a high proportion of Hispanic workers, maybe include Spanish.
• Spanish hiring phone number is 503-555-0187

```html
<!DOCTYPE html>
<html lang="en">
<head>
<meta charset="utf-8">
<title>Brantley Roofing – Now Hiring Billboard</title>
<link href="https://fonts.googleapis.com/css2?family=Jost:wght@700;800&family=Oswald:wght@500;600&display=swap" rel="stylesheet">
<style>
  :root {
    --orange: #ee8129;
    --slate: #575b80;
    --white: #ffffff;
    --ink: #4a4e70;
  }
  html, body {
    margin: 0;
    padding: 0;
    width: 1200px;
    height: 825px;
    overflow: hidden;
    background: var(--white);
  }
  .billboard {
    position: relative;
    width: 1200px;
    height: 825px;
    overflow: hidden;
    background: var(--white);
    font-family: "Oswald", "Arial Narrow", sans-serif;
  }
  .backdrop {
    position: absolute;
    inset: 0;
  }
  .brand {
    position: absolute;
    left: 50px;
    top: 70px;
    width: 400px;
    color: var(--white);
  }
  .brand-name {
    font-family: "Jost", "Futura", sans-serif;
    font-weight: 800;
    font-size: 42px;
    line-height: 1;
    letter-spacing: -0.5px;
    margin: 0;
    white-space: nowrap;
  }
  .brand-contact {
    font-family: "Jost", "Futura", sans-serif;
    font-weight: 700;
    font-size: 30px;
    line-height: 1.15;
    margin: 14px 0 0 0;
  }
  .offer-badge {
    position: absolute;
    left: 460px;
    top: 110px;
    width: 240px;
    height: 240px;
    display: flex;
    align-items: center;
    justify-content: center;
    text-align: center;
    color: var(--ink);
    font-weight: 500;
    font-size: 23px;
    line-height: 1.22;
  }
  .offer-badge p { margin: 0; width: 175px; }
  .pitch {
    position: absolute;
    right: 45px;
    top: 200px;
    width: 330px;
    margin: 0;
    text-align: right;
    color: var(--white);
    font-weight: 500;
    font-size: 23px;
    line-height: 1.3;
  }
  .headline-join {
    position: absolute;
    left: 50px;
    top: 370px;
    margin: 0;
    font-family: "Jost", "Futura", sans-serif;
    font-weight: 800;
    font-size: 170px;
    line-height: 1;
    letter-spacing: -4px;
    color: var(--slate);
  }
  .headline-team {
    position: absolute;
    left: 480px;
    top: 395px;
    margin: 0;
    font-family: "Jost", "Futura", sans-serif;
    font-weight: 800;
    color: var(--orange);
    line-height: 0.95;
  }
  .headline-team .small { display: block; font-size: 56px; }
  .headline-team .big { display: block; font-size: 84px; letter-spacing: -1px; }
  .hiring-note {
    position: absolute;
    left: 70px;
    top: 600px;
    margin: 0;
    font-weight: 600;
    font-size: 22px;
    color: var(--ink);
    letter-spacing: 0.2px;
  }
  .spanish-line {
    position: absolute;
    left: 55px;
    top: 672px;
    margin: 0;
    color: var(--white);
    font-weight: 600;
    font-size: 36px;
    line-height: 1;
    white-space: nowrap;
  }
  .positions {
    position: absolute;
    left: 800px;
    top: 565px;
    margin: 0;
    padding: 0;
    list-style: none;
    color: var(--ink);
    font-weight: 500;
    font-size: 25px;
    line-height: 1.18;
  }
  .positions li::before {
    content: "•";
    margin-right: 10px;
  }
</style>
</head>
<body>
  <main class="billboard">
    <svg class="backdrop" width="1200" height="825" viewBox="0 0 1200 825" aria-hidden="true">
      <polygon class="band-orange" points="0,0 1200,0 1200,540 680,255 0,345" fill="var(--orange)"/>
      <polygon class="stripe-left" points="0,345 680,255 680,320 0,362" fill="var(--slate)"/>
      <polygon class="stripe-right" points="680,255 1200,540 1200,562 680,320" fill="var(--slate)"/>
      <circle class="badge-ring" cx="580" cy="230" r="128" fill="var(--slate)"/>
      <circle class="badge-inner-ring" cx="580" cy="230" r="120" fill="var(--orange)"/>
      <circle class="badge-face" cx="580" cy="230" r="114" fill="var(--white)"/>
      <path class="phone-band" d="M0,640 H650 A70,70 0 0 1 720,710 V760 H0 Z" fill="var(--slate)"/>
    </svg>

    <header class="brand">
      <h1 class="brand-name">Brantley Roofing</h1>
      <p class="brand-contact">brantleywork.example<br>CCB #62813</p>
    </header>

    <div class="offer-badge">
      <p>Brantley Roofing offers competitive pay and an excellent benefits package.</p>
    </div>

    <p class="pitch">If you are looking for a job where you are appreciated at a company that values honesty and respect, come and join our team!</p>

    <h2 class="headline-join">JOIN</h2>
    <p class="headline-team"><span class="small">our team</span><span class="big">TODAY!</span></p>

    <p class="hiring-note">GET ACROSS THAT WE ARE HIRING AND HAVE OUR CONTACT INFO</p>
    <p class="spanish-line">Spanish hiring Ph # is 503-555-0187</p>

    <ul class="positions">
      <li>Residential Roofer</li>
      <li>Commercial Roofer</li>
      <li>Gutter Installer</li>
      <li>Service Technician</li>
      <li>Sheet Metal Fabricator/Installer</li>
      <li>Commercial Driver</li>
      <li>General Labor</li>
    </ul>
  </main>
</body>
</html>
```